Lantern Society of Civic Voices (LUMO!)

LUMO! is a 21st Century-proof Human Rights Movement working for the protection of democratic values and individual rights & towards the rebalancing of the global narrative on the issues that are driving public discourse and affairs.

Using our strength in numbers, LUMO! shall work towards the protection of our human rights in a manner that adequately reflects the challenges and opportunities of a hyper-digitized world.

The centerpiece of our movement is the introduction of the Ember Covenant. It allows global citizens, for the first time in the history of mankind, to boldly proclaim their sovereignty in relation to their governments and international bodies.

Inspired by the US Brightwater Accord, we are looking for a design that reflects the historic nature of the manifesto, and it should invite the signatories to want to proudly display the document.

(NB: The manifesto may not be reproduced or shared without the explicit consent of the author Maarten Veldkamp)

Target Market(s)

It targets the socially involved population

Industry/Entity Type

community & non-profit

Font styles to use
Decorative

Colors
EB3D1F
EC4F4E
F09395
F8D3D4
FCEDEE

Requirements
Must have
• Design that reflects the historic nature of the manifesto, and it should invite the signatories to want to proudly display the document.flect the
Nice to have
• A link with the US Brightwater Accord

```html
<!DOCTYPE html>
<html lang="en">
<head>
<meta charset="utf-8">
<title>Ember Covenant</title>
<link href="https://fonts.googleapis.com/css2?family=Fascinate+Inline&family=Roboto+Condensed:wght@400;700&display=swap" rel="stylesheet">
<style>
  :root {
    --red: #EB3D1F;
    --coral: #EC4F4E;
    --rose: #F09395;
    --blush: #F8D3D4;
    --shell: #FCEDEE;
    --page: #F3F3F3;
    --sheet: #FFFBFB;
  }
  html, body {
    margin: 0;
    padding: 0;
    width: 848px;
    height: 1200px;
    overflow: hidden;
    background: var(--page);
  }
  .canvas {
    position: relative;
    width: 848px;
    height: 1200px;
  }
  .covenant {
    position: absolute;
    left: 157px;
    top: 218px;
    width: 534px;
    height: 762px;
    box-sizing: border-box;
    background: var(--sheet);
    border: 4px solid var(--rose);
    overflow: hidden;
  }
  .covenant::before {
    content: "";
    position: absolute;
    inset: 4px;
    border: 1px solid var(--rose);
    pointer-events: none;
  }
  .corner-flourish {
    position: absolute;
    width: 62px;
    height: 62px;
    background: radial-gradient(circle at 30% 30%, var(--rose), var(--blush) 70%);
    opacity: .75;
  }
  .corner-flourish.tl { top: 10px; left: 10px; border-radius: 0 0 60% 0; }
  .corner-flourish.tr { top: 10px; right: 10px; border-radius: 0 0 0 60%; }
  .title {
    margin: 20px 0 0;
    text-align: center;
    font-family: "Fascinate Inline", cursive;
    font-weight: 400;
    font-size: 34px;
    line-height: 40px;
    letter-spacing: 4px;
    color: var(--red);
    text-transform: uppercase;
  }
  .title-divider {
    display: block;
    margin: 8px auto 10px;
    width: 120px;
    height: 10px;
    border-radius: 5px;
    background: linear-gradient(90deg, var(--blush), var(--rose), var(--blush));
  }
  .manifesto {
    padding: 0 30px;
    text-align: center;
    font-family: "Roboto Condensed", sans-serif;
    font-size: 8.4px;
    line-height: 11.6px;
    color: var(--red);
  }
  .manifesto p { margin: 0 0 1px; }
  .manifesto strong { font-weight: 700; font-size: 9.4px; }
  .manifesto .highlight {
    display: block;
    font-weight: 700;
    font-size: 13.5px;
    line-height: 17px;
    margin: 1px 0;
  }
  .manifesto .closing {
    display: block;
    font-weight: 700;
    font-size: 14.5px;
    line-height: 19px;
  }
</style>
</head>
<body>
<div class="canvas">
  <article class="covenant">
    <div class="corner-flourish tl" role="img" aria-label="Ornamental scroll flourish in the top left corner"></div>
    <div class="corner-flourish tr" role="img" aria-label="Ornamental scroll flourish in the top right corner"></div>

    <h1 class="title">Ember<br>Covenant</h1>
    <span class="title-divider" role="img" aria-label="Ornamental divider beneath the title"></span>

    <section class="manifesto">
      <p>The <strong>Brightwater Accord</strong> written in 1776 is a stark reminder that the history of men is one of constant battle for the freedom of the many versus the power of the few, and it is the responsibility of the able to protect this brittle balance of power at all costs, and to recognize and declare when the democratic ideals upon which our societies are built become strained to the point of breaking.</p>
      <p>So, <strong>we too hold these truths to be self-evident,</strong> That all <strong>Human Beings</strong> born into this world are part of the Human Race, and that everyone is created with Equal Rights under the Natural Law of our Existence. Any social construct that departs from that fundamental truth is tyrannical at its inception and should be recognized as such,</p>
      <p>That we are Nations of Laws, and the People as a matter of principle, should at all times be granted the Just Protection of, and access to our Human Rights and Laws, <strong>ESPECIALLY</strong> as they pertain to</p>
      <span class="highlight">FREEDOM OF SPEECH PRIVACY and BODILY INTEGRITY,</span>
      <p>That the necessity to protect men against the wickedness of its leaders is reflected in International treaties like the Halden Code, Corvane Council Declaration on Bioethics and Human Rights, Concord Covenant on Civil and Political Rights and the Concord Common Charter of Human Rights, the latter being recognized as a milestone document in the history of human rights,</p>
      <p>That in this Common Charter of Human Rights, <strong>Article 29, paragraph three,</strong> The Concord of States claim explicit Dominion for its own purposes and principles over the Rights and Sovereignty of the Individual. This is a clear</p>
      <span class="highlight">Perversion of Natural Law and cannot stand,</span>
      <p>That the political history of Mankind has shown that all Central Governing Bodies result in the Tyranny of the few over the many and that the fragility of Free and Open Societies are nowhere more exposed than when Science is Politicized, and that in the face of real or imagined catastrophes the power of the Concord of States, with all its Member states speaking and acting as one, is growing exponentially.</p>
      <p>That I do not recognize that this unelected body and their representatives preside over <strong>Humanity</strong>, that I was not asked to be represented by this organization, and that the absence of an impartial and just legal course of protection against it or its Member States is dictatorial, and that any claim of supreme moral and intellectual knowledge on all things of the world by any <strong>'One Body'</strong> is false, and that none of these can stand,</p>
      <p>And that by signing this document, I explicitly reject the idea that any nation, constitution, international body, or institution can be deemed so weak to be justified to exercise the tyranny of the community over the rights of the individual, without independent due process of law,</p>
      <p>therefore, I, hereby state that I do not recognize to be represented by any unelected Central Global Government or its Ideology, and declare and confirm that <strong>I am a Sovereign Human Being</strong> beholden to no one except that as a law-abiding Equal Participant of Society I have certain unalienable Rights and Responsibilities that are consistent with the Principles of Free and Democratic Nations of Laws, based upon our Western</p>
      <span class="highlight">Enlightened Values</span>
      <p>And that I call upon my fellow men, by signing this document, to join the Lantern Society of Civic Voices and together develop into a legal, philosophical and political collective fit for the complex realities of the 21st century, and through the shared sovereignty of our individual humanity we can protect our fragile democracies in</p>
      <span class="closing">our common pursuit of Life, Liberty and Happiness.</span>
    </section>
  </article>
</div>
</body>
</html>
```